Mobile Repair Service on location needs a Web Design

We are starting a new mobile device repair service called Gadget Haven and our website needs a design!

Hello Designers!
First, we'd like to make clear this is more than a simple web design contest, we want the designers to create an idea. We want someone who can create the whole theme of the service's we provide. We want someone that can help design our visual branding, help us communicate a sentiment. And we are willing to pay for that.

Who are we?
Our company is based in Rotterdam, the Netherlands. We provide different services for all kinds of electronic devices. The kind of services we provide are, among other things, installations of hardware and software and the repair of broken or malfunctioning devices.
We are starting a new service that offers mobile device repairs on location, be it at the home of our customers, their office, or any other place. Just give us the address and we will come to you for the repair job. This is also our main USP. We have multiple skilled engineers who drive trough the country on a daily basis and can be on location within a working day. Repair is done immediately onsite while the customer waits. At this stage we will start with the smartphone product-group within the mobile devices. In a second phase we might also add tablets.
People don't want to be without their phone for weeks because of some parts that needed to be ordered by a repair center they had to sent their phone to. We offer a fully functional mobile repair center in the form of specially customized vans. These vans have all the tools and utilities needed by our engineers to safely repair your mobile device. Your phone is being repaired directly in front of you, the next business-day, on a location you desire.

For this new service we are creating a website called Gadget Haven. The website needs a story and matching design and this is where you come in. We are not looking for a simple template design we can get from any place. We need a story. We want you to create an idea, build a unique theme or vision that helps sell the product/service. This goes beyond the design of the website. We need the whole package, the design you are creating needs to have returning elements like icons, color use, images, maybe even characters etc. You name it! There needs to be a common thread in the design so we can reuse elements in, for example, the email templates, the work order or receipt we give to our customers (we may contact the winner of the contest to design these for us as well!).

The name 'Gadget Haven' is chosen. Haven (short for rehabilitate) has a bold and playful tone to it and the design needs to reflect the name. So we're looking for a somewhat playful and cheeky design. Definitely not too serious and definitely modern. We already got a logo that we love and that fit's this description (see attached design documents for the logo). It's bold, powerful and fun. Our web design needs to reflect this as well and has to fit in with our logo.
We would really like it if the design somehow incorporates elements that highlight our unique selling points (repairs on location, we come to you etc.). We would really like some form of story telling in the design. Think clumsy people breaking their phones. Teenagers in tears because they have no access to their friends. People nowadays have the need to always be 'connected'. What happens when your phone is broken or malfunctioning? We're handling tech, we are nerds and a little bit weird, but we're professionals and here to help you with your problem. The sentiment Wire Troop tries to communicate is something we really like. We're looking for fresh idea's, anything goes!

In an overview all Unique Selling Points of the Gadget haven service:
- Professional service on location. Don’t ship to us we will come to you!
- Clear pricing upfront. No hidden cost.
- Next business-day repair.
- Backed by a professional call center open 12 hours a day and open on a Saturday as well
- Backed by a professional repair center with more then 12 years of experience
- Repair is done by certified engineers
- 1 year warranty on the repair

The process:
The main function of our website will be for customers to make a repair request. A customer will visit our website and can make a repair request immediately by going through a 'request-order-flow'. In this flow he or she will need to fill in some forms and can select wich type/model/brand of mobile device he or she has and what parts need to be repaired. After a request is placed we will call the customer back (within an hour) for a short intake and to set a date/time and location. Our engineer will meet the customer at the specified location and will repair the device onsite in one of our mobile repair centers, which is a specialized van equipped with all the tools needed for device restorations.
So in short the steps are:
- Choose your device and repair job
- Place the order
- Get a callback within the hour
- Set date and location
- We will come to you.

Website functionality:
Our website is our main form of communication. So the sentiment we want to communicate needs be reflected in the design. We need a main/front page designed (preferably a long scrolling page design) containing:
1. Customers will be able to request a repair job directly on our website. So there will need to be a prominent button/link at the top of our main page that will bring the customer to this 'request-order-flow'. This is the main flow which needs to be full focus on the front page. All other items are secondary.
2. The general information of who we are and what we do, and why the customer should choose us. Preferably in short bullet-point type keywords/sentences with icons or other visual cues. See our unique selling points to get an idea of the information that will be displayed here.
3. There needs to be a section that will explain the process (see above) of a repair request step-by- step, again in brief short key sentences and with (custom) icons.
4. There needs to be a section that explains to the customer he/she can always contact us if they are not sure what the problem is with their device, and for this reason are not sure what repair request they should order.
5. We want to implement some functionality that display customer ratings or customer reviews. So there needs to be room for some kind of widget of plugin we're going to implement which shows these reviews.
6. A 'For business section' where we will explain all the options we provide for corporate clients.
7. Social media links.
8. There needs to be a menu with buttons that leads to the all sections described in the previous points.

For now, we need a design for our front page. In the second phase, when we have picked our winner, we may ask the winner to design the page(s) for our request workflow as well.

EDIT:
Finally, we have a very specific order in mind for the different segments of our website. We would like you to add some more segments that were not in our original brief as well:

1. Top header with order/request button. (should instantly make clear our main USP, we do repairs on location)
2. Our process
3. Our unique selling points / why choose us
4. The kind of repairs we do (broken screens, broken batteries, water damage, broken camera's, no sound etc.)
5. A 'meet our team' section, where we introduce some of our engineers
6. A 'contact us for any questions' section/
7. Testimonials/user reviews
8. A section where we show key performance indicators
9. 'For businesses' sections
10.'Subscribe for newsletter' field
11. Social media buttons

Industry/Entity Type

It Service

Number of Pages Required

1 page

Font styles to use
Sans Serif

Requirements
Must have
• a main/front page, design only
• custom icons/images for banners, adverts online and in print (high res)
Nice to have
• Storytelling in our design.
• Design that fits with our brand new logo.
• Elements like icons to have a flat design.
• Keep in mind that the website will need to be responsive when designing! (Ideally provide an example of the mobile design as well)
• Create a fun and trustworthy feeling.

```html
<!DOCTYPE html>
<html lang="en">
<head>
<meta charset="utf-8">
<title>Gadget Haven – Mobile Repair On Location</title>
<link href="https://fonts.googleapis.com/css2?family=Lato:wght@400;700;900&family=Open+Sans:wght@400;600;700&display=swap" rel="stylesheet">
<style>
:root{
  --orange:#e85b24;
  --orange-dark:#d44d18;
  --ink:#1f1f1f;
  --text:#444;
  --muted:#666;
  --light:#f1f1f1;
  --line:#dcdcdc;
  --white:#fff;
}
*{box-sizing:border-box;margin:0;padding:0}
html,body{width:1200px;height:3158px;overflow:hidden}
body{font-family:"Open Sans",Arial,sans-serif;color:var(--text);background:var(--white);position:relative}
.abs{position:absolute}
.heading{font-family:"Lato",Arial,sans-serif}

/* Header */
.site-header{position:absolute;left:0;top:0;width:1200px;height:105px}
.brand{position:absolute;left:100px;top:24px;display:flex;align-items:center;gap:12px}
.brand-dot{width:52px;height:52px;border-radius:50%;background:var(--orange)}
.brand-name{font-family:"Lato",sans-serif;font-weight:900;font-size:24px;line-height:25px;color:var(--ink);width:110px}
.search{position:absolute;left:410px;top:36px;width:327px;height:42px;border:1px solid #cfcfcf;display:flex;align-items:center;justify-content:space-between;padding:0 14px;font-size:14px;color:#888}
.cart{position:absolute;left:760px;top:36px;display:flex;align-items:center;gap:12px;font-size:17px;color:var(--ink);font-weight:600}
.cart-icon{width:38px;height:38px;border-radius:50%;background:var(--orange);display:flex;align-items:center;justify-content:center}
.btn{background:var(--orange);color:var(--white);font-size:14px;display:flex;align-items:center;justify-content:center;font-weight:600}
.order-btn{position:absolute;left:941px;top:34px;width:158px;height:40px;font-size:14px}

/* Nav */
.main-nav{position:absolute;left:0;top:105px;width:1200px;height:55px;background:var(--orange)}
.nav-left,.nav-right{position:absolute;top:0;height:55px;display:flex;align-items:center}
.nav-left{left:99px}
.nav-left a{color:var(--white);text-decoration:none;font-size:15px;width:160px;height:55px;display:flex;align-items:center;justify-content:center;font-weight:600}
.nav-left a.active{background:var(--orange-dark)}
.nav-left a+ a{width:120px}
.nav-right{left:590px;width:511px;background:var(--orange-dark);justify-content:space-around;padding:0 10px}
.nav-right a{color:var(--white);text-decoration:none;font-size:15px}

/* Hero */
.hero{position:absolute;left:0;top:164px;width:1200px;height:510px;background:#efefef}
.hero-scene{position:absolute;left:0;top:0;width:1200px;height:510px;background:linear-gradient(180deg,#f2f2f2 0%,#ececec 55%,#dedede 100%)}
.hero-title{position:absolute;right:99px;top:50px;text-align:right;color:var(--orange);font-weight:700;font-size:35px}
.hero-sub{position:absolute;right:99px;top:102px;text-align:right;color:var(--ink);font-weight:700;font-size:26px}
.hero-btn{position:absolute;left:831px;top:173px;width:268px;height:57px;font-size:16px}
.slide-arrow{position:absolute;top:230px}

/* Section titles */
.section-title{position:absolute;left:0;width:1200px;text-align:center;font-family:"Lato",sans-serif;font-weight:700;color:var(--orange);font-size:31px}

/* Who */
.who-sub{position:absolute;left:0;width:1200px;top:782px;text-align:center;font-size:20px;color:var(--ink);font-weight:600}
.who-text{position:absolute;left:120px;top:836px;width:960px;text-align:center;font-size:13.5px;line-height:28px;color:#333}
.feature{position:absolute;top:955px;width:200px;text-align:center}
.feature-bubble{margin:0 auto;width:139px;height:160px}
.feature h3{font-family:"Open Sans",sans-serif;font-weight:600;font-size:17px;color:var(--ink);margin-top:30px}
.feature.active h3{color:var(--orange)}
.feature p{font-size:12.5px;line-height:22px;color:#444;margin-top:10px}

/* How */
.how{position:absolute;left:0;top:1280px;width:1200px;height:505px;background:var(--orange)}
.how h2{position:absolute;top:52px;left:0;width:1200px;text-align:center;color:var(--white);font-family:"Lato",sans-serif;font-weight:700;font-size:30px}
.how-rule{position:absolute;left:565px;top:101px;width:70px;height:2px;background:var(--white)}
.step{position:absolute;width:130px;height:130px;border-radius:50%;background:var(--white);display:flex;align-items:center;justify-content:center}
.step-label{position:absolute;width:260px;text-align:center;color:var(--white);font-size:16px;line-height:28px;font-weight:600}

/* Services */
.services-title{position:absolute;left:99px;top:1843px;font-family:"Lato",sans-serif;font-weight:700;color:var(--orange);font-size:27px}
.service-item{position:absolute;left:99px;width:620px;display:flex;gap:22px;font-size:14.5px;line-height:28px;color:#333}
.service-item svg{flex:none;margin-top:2px}
.services-btn{position:absolute;left:158px;top:2166px;width:210px;height:46px;font-size:15px}
.services-photo{position:absolute;left:768px;top:1895px;width:432px;height:284px;background:linear-gradient(135deg,#f5f5f5,#d9d4d0 60%,#f2dcd2)}

/* Testimonials */
.testimonials{position:absolute;left:0;top:2284px;width:1200px;height:474px;background:var(--light)}
.quote{position:absolute;top:189px;width:322px;height:173px;border:2px solid var(--orange);background:var(--white);padding:36px 22px 0;font-size:13.5px;line-height:24px;color:#222}
.quote.featured{background:var(--orange);color:var(--white)}
.quote-icon{position:absolute;top:-19px;left:50%;margin-left:-19px;width:38px;height:38px;border-radius:50%;background:var(--orange);border:3px solid var(--light);display:flex;align-items:center;justify-content:center}
.quote-tail{position:absolute;left:14px;bottom:-22px}
.quote-name{position:absolute;top:380px;color:var(--orange);font-size:15px;font-weight:600}

/* Footer */
.site-footer{position:absolute;left:0;top:2758px;width:1200px;height:347px;border-top:3px solid var(--orange)}
.footer-brand{position:absolute;left:99px;top:62px;width:120px;text-align:center}
.footer-brand .brand-dot{width:96px;height:96px;margin:0 auto}
.footer-brand .name{font-family:"Lato",sans-serif;font-weight:900;font-size:27px;line-height:30px;color:var(--ink);margin-top:14px}
.footer-brand .tag{font-size:11px;color:#1f4fa0;font-weight:700;margin-top:4px}
.footer-col h4{font-family:"Lato",sans-serif;font-weight:700;color:var(--orange);font-size:17px;margin-bottom:22px}
.footer-col{position:absolute;top:62px}
.links li{list-style:none;font-size:14px;line-height:31.5px;color:#333}
.contact-row{display:flex;gap:16px;margin-bottom:20px;font-size:12.5px;line-height:18px;color:#333}
.contact-row b{font-size:14px;color:var(--ink)}
.c-icon{flex:none;width:36px;height:36px;border:2px solid var(--orange);border-radius:50%;display:flex;align-items:center;justify-content:center}
.field{position:absolute;border:1px solid #bdbdbd;font-size:11px;color:#444;padding:8px 8px}
.send-btn{position:absolute;left:815px;top:231px;width:115px;height:36px;font-size:12px}

.bottom-bar{position:absolute;left:0;top:3105px;width:1200px;height:53px;border-top:1px solid var(--line)}
.copyright{position:absolute;left:99px;top:16px;font-size:14px;color:#222}
.socials{position:absolute;left:875px;top:8px;display:flex;gap:12px}
.socials span{width:36px;height:36px;border:2px solid #333;border-radius:50%}
</style>
</head>
<body>

<header class="site-header">
  <div class="brand"><div class="brand-dot"></div><div class="brand-name">GADGET HAVEN</div></div>
  <div class="search">Search
    <svg width="14" height="14" viewBox="0 0 14 14"><circle cx="6" cy="6" r="4.5" fill="none" stroke="#333" stroke-width="1.6"/><line x1="9.3" y1="9.3" x2="13" y2="13" stroke="#333" stroke-width="1.8"/></svg>
  </div>
  <div class="cart">
    <div class="cart-icon"><svg width="18" height="16" viewBox="0 0 18 16"><rect x="2" y="5" width="14" height="10" rx="1.5" fill="#fff"/><path d="M6 5V3a3 3 0 0 1 6 0v2" fill="none" stroke="#fff" stroke-width="1.6"/></svg></div>
    CART: 0 Items
  </div>
  <a class="btn order-btn">Request Order Flow</a>
</header>

<nav class="main-nav">
  <div class="nav-left"><a class="active">PRODUCTS</a><a>BRANDS</a><a>DEALS</a></div>
  <div class="nav-right"><a>Weekly Ad</a><a>Deal of the Day</a><a>Gift Cards</a><a>Gift Ideas &amp; Registry</a></div>
</nav>

<section class="hero">
  <div class="hero-scene" role="img" aria-label="Photo of a call center agent with a headset beside a black service car carrying the Gadget Haven name"></div>
  <h1 class="hero-title heading">PROFESSIONAL SERVICE ON LOCATION</h1>
  <p class="hero-sub heading">DON’T SHIP TO US WE WILL COME TO YOU!</p>
  <a class="btn hero-btn">1 YEAR WARRANTY ON REPAIR</a>
  <svg class="slide-arrow" style="left:36px" width="24" height="48" viewBox="0 0 24 48"><polyline points="22,2 2,24 22,46" fill="none" stroke="#777" stroke-width="2"/></svg>
  <svg class="slide-arrow" style="left:1140px" width="24" height="48" viewBox="0 0 24 48"><polyline points="2,2 22,24 2,46" fill="none" stroke="#777" stroke-width="2"/></svg>
</section>

<section class="who">
  <h2 class="section-title" style="top:730px">WHO ARE WE?</h2>
  <p class="who-sub">Clear pricing upfront. No hidden cost.</p>
  <p class="who-text">Our company is based in Rotterdam, the Netherlands. We provide different services for all kinds of electronic devices. The kind of services we provide are, among other things, installations of hardware and software and the repair of broken or malfunctioning devices. We are starting a new service that offers mobile device repairs on location, be it at the home of our customers, their office, or any other place.</p>

  <div class="feature" style="left:85px">
    <svg class="feature-bubble" viewBox="0 0 139 160"><path d="M69.5 2a67.5 67.5 0 0 1 18 132.6L69.5 156 51.5 134.6A67.5 67.5 0 0 1 69.5 2z" fill="#fff" stroke="#e85b24" stroke-width="2.5"/><circle cx="69.5" cy="60" r="20" fill="#e85b24"/><path d="M45 100c4-16 14-20 24.5-20S90 84 94 100z" fill="#e85b24"/><path d="M47 56a22.5 22.5 0 0 1 45 0z" fill="#fff" stroke="#e85b24" stroke-width="3"/></svg>
    <h3>Good Professionals</h3><p>These vans have all the tools and utilities needed.</p>
  </div>
  <div class="feature active" style="left:292px">
    <svg class="feature-bubble" viewBox="0 0 139 160"><path d="M69.5 2a67.5 67.5 0 0 1 18 132.6L69.5 156 51.5 134.6A67.5 67.5 0 0 1 69.5 2z" fill="#e85b24" stroke="#e85b24" stroke-width="2.5"/><path d="M55 48c-4 4-2 14 8 24s20 12 24 8l3-4-8-7-5 4c-4-2-9-7-11-11l4-5-7-8z" fill="#fff"/><path d="M72 46a14 14 0 0 1 14 14M72 39a21 21 0 0 1 21 21" fill="none" stroke="#fff" stroke-width="3"/></svg>
    <h3>Repair And Service</h3><p>Your phone is being repaired directly in front of you.</p>
  </div>
  <div class="feature" style="left:502px">
    <svg class="feature-bubble" viewBox="0 0 139 160"><path d="M69.5 2a67.5 67.5 0 0 1 18 132.6L69.5 156 51.5 134.6A67.5 67.5 0 0 1 69.5 2z" fill="#fff" stroke="#e85b24" stroke-width="2.5"/><rect x="54" y="36" width="31" height="52" rx="4" fill="none" stroke="#e85b24" stroke-width="4"/><rect x="59" y="43" width="21" height="34" fill="#e85b24"/></svg>
    <h3>Cell Phones</h3><p>The next business-day, on a location you.</p>
  </div>
  <div class="feature" style="left:710px">
    <svg class="feature-bubble" viewBox="0 0 139 160"><path d="M69.5 2a67.5 67.5 0 0 1 18 132.6L69.5 156 51.5 134.6A67.5 67.5 0 0 1 69.5 2z" fill="#fff" stroke="#e85b24" stroke-width="2.5"/><rect x="42" y="44" width="44" height="30" rx="2" fill="none" stroke="#e85b24" stroke-width="4"/><path d="M36 80h56" stroke="#e85b24" stroke-width="4"/><rect x="86" y="52" width="18" height="30" rx="2" fill="#fff" stroke="#e85b24" stroke-width="4"/></svg>
    <h3>Computer &amp; Tablets</h3><p>This new service we are creating a website called Gadget Haven.</p>
  </div>
  <div class="feature" style="left:917px">
    <svg class="feature-bubble" viewBox="0 0 139 160"><path d="M69.5 2a67.5 67.5 0 0 1 18 132.6L69.5 156 51.5 134.6A67.5 67.5 0 0 1 69.5 2z" fill="#fff" stroke="#e85b24" stroke-width="2.5"/><rect x="50" y="42" width="36" height="46" rx="3" fill="none" stroke="#e85b24" stroke-width="4"/><path d="M58 58h20M58 66h20M58 74h14" stroke="#e85b24" stroke-width="3.5"/><circle cx="86" cy="42" r="11" fill="#e85b24"/><path d="M86 36v12M80 42h12" stroke="#fff" stroke-width="2.5"/></svg>
    <h3>Pricing &amp; Deals</h3><p>We want you to create an idea, build a unique theme.</p>
  </div>
</section>

<section class="how">
  <h2>HOW IT WORKS</h2>
  <div class="how-rule"></div>

  <div class="step" style="left:93px;top:206px"><svg width="60" height="60" viewBox="0 0 60 60"><circle cx="30" cy="30" r="20" fill="none" stroke="#e85b24" stroke-width="6" stroke-dasharray="7 4"/><circle cx="30" cy="30" r="9" fill="none" stroke="#e85b24" stroke-width="4"/></svg></div>
  <div class="step" style="left:339px;top:278px"><svg width="56" height="60" viewBox="0 0 56 60"><rect x="8" y="8" width="34" height="46" rx="3" fill="#e85b24"/><path d="M15 26h20M15 34h20M15 42h14" stroke="#fff" stroke-width="3"/><circle cx="42" cy="12" r="10" fill="#fff" stroke="#e85b24" stroke-width="3"/><path d="M42 7v10M37 12h10" stroke="#e85b24" stroke-width="2.5"/></svg></div>
  <div class="step" style="left:571px;top:206px"><svg width="60" height="60" viewBox="0 0 60 60"><path d="M14 12c-6 6-4 18 10 32s26 16 32 10l2-4-10-9-6 5c-6-3-12-9-14-14l5-6-9-10z" fill="none" stroke="#e85b24" stroke-width="4"/><path d="M36 10v12h12M36 22l14-14" stroke="#e85b24" stroke-width="4" fill="none"/></svg></div>
  <div class="step" style="left:802px;top:278px"><svg width="50" height="60" viewBox="0 0 50 60"><path d="M25 6a15 15 0 0 1 15 15c0 12-15 27-15 27S10 33 10 21A15 15 0 0 1 25 6z" fill="none" stroke="#e85b24" stroke-width="4"/><circle cx="25" cy="21" r="5" fill="#e85b24"/><ellipse cx="25" cy="52" rx="16" ry="4" fill="none" stroke="#e85b24" stroke-width="3"/></svg></div>
  <div class="step" style="left:1009px;top:206px"><svg width="56" height="56" viewBox="0 0 56 56"><path d="M26 8h22v40H26" fill="none" stroke="#e85b24" stroke-width="4"/><rect x="30" y="12" width="14" height="32" fill="#e85b24"/><path d="M6 28h24M20 18l10 10-10 10" fill="none" stroke="#e85b24" stroke-width="4"/></svg></div>

  <svg class="abs" style="left:248px;top:282px" width="80" height="60" viewBox="0 0 80 60"><path d="M4 6c30 0 48 14 58 42" fill="none" stroke="#fff" stroke-width="2"/><path d="M54 42l8 8 4-11" fill="none" stroke="#fff" stroke-width="2"/></svg>
  <svg class="abs" style="left:485px;top:256px" width="80" height="60" viewBox="0 0 80 60"><path d="M4 54C10 24 34 8 70 8" fill="none" stroke="#fff" stroke-width="2"/><path d="M62 2l9 6-8 7" fill="none" stroke="#fff" stroke-width="2"/></svg>
  <svg class="abs" style="left:720px;top:282px" width="80" height="60" viewBox="0 0 80 60"><path d="M4 6c30 0 48 14 58 42" fill="none" stroke="#fff" stroke-width="2"/><path d="M54 42l8 8 4-11" fill="none" stroke="#fff" stroke-width="2"/></svg>
  <svg class="abs" style="left:935px;top:256px" width="80" height="60" viewBox="0 0 80 60"><path d="M4 54C10 24 34 8 70 8" fill="none" stroke="#fff" stroke-width="2"/><path d="M62 2l9 6-8 7" fill="none" stroke="#fff" stroke-width="2"/></svg>

  <p class="step-label" style="left:28px;top:360px">Choose your device and<br>repair job</p>
  <p class="step-label" style="left:274px;top:232px">Place the order</p>
  <p class="step-label" style="left:506px;top:360px">Get a callback within<br>the hour</p>
  <p class="step-label" style="left:737px;top:216px">Set date and<br>location</p>
  <p class="step-label" style="left:944px;top:360px">We will come to<br>you</p>
</section>

<section class="services">
  <h2 class="services-title">OUR GADGET HAVEN SERVICES</h2>
  <div class="service-item" style="top:1918px">
    <svg width="34" height="30" viewBox="0 0 34 30"><path d="M6 4c-4 4-2 11 6 19s15 10 19 6l1-3-6-5-4 3c-3-1-7-5-8-8l3-4-5-6z" fill="#e85b24"/></svg>
    <span>Backed by a professional call center open 12 hours a day and open on a Saturday as well.</span>
  </div>
  <div class="service-item" style="top:1988px">
    <svg width="34" height="30" viewBox="0 0 34 30"><circle cx="15" cy="15" r="10" fill="none" stroke="#e85b24" stroke-width="5" stroke-dasharray="4 3"/><circle cx="15" cy="15" r="4" fill="#e85b24"/></svg>
    <span>Backed by a professional repair center with more then 12 years of experience</span>
  </div>
  <div class="service-item" style="top:2043px">
    <svg width="34" height="30" viewBox="0 0 34 30"><circle cx="15" cy="9" r="6" fill="#e85b24"/><path d="M4 29c1-9 5-12 11-12s10 3 11 12z" fill="#e85b24"/></svg>
    <span>Repair is done by certified engineers</span>
  </div>
  <div class="service-item" style="top:2106px">
    <svg width="34" height="30" viewBox="0 0 34 30"><circle cx="15" cy="11" r="8" fill="none" stroke="#e85b24" stroke-width="3"/><path d="M10 17l-3 12 8-4 8 4-3-12" fill="none" stroke="#e85b24" stroke-width="3"/></svg>
    <span>1 year warranty on the repair</span>
  </div>
  <a class="btn services-btn">Next business-day repair</a>
  <div class="services-photo" role="img" aria-label="Photo of hands repairing an opened smartphone with a small tool"></div>
</section>

<section class="testimonials">
  <h2 class="section-title" style="top:54px">CLIENT TESTIMONIALS</h2>
  <svg class="abs" style="left:40px;top:268px" width="16" height="32" viewBox="0 0 16 32"><polyline points="14,2 2,16 14,30" fill="none" stroke="#555" stroke-width="2"/></svg>
  <svg class="abs" style="left:1143px;top:268px" width="16" height="32" viewBox="0 0 16 32"><polyline points="2,2 14,16 2,30" fill="none" stroke="#555" stroke-width="2"/></svg>

  <div class="quote" style="left:99px">
    <div class="quote-icon"><svg width="18" height="16" viewBox="0 0 18 16"><path d="M2 2h14v9H7l-4 4v-4H2z" fill="#fff"/></svg></div>
    “Nemo enim ipsam voluptatem quia voluptas sit aspernatur aut odit aut fugit, sed quia con sequuntur magni dolores eos qui ratione vo luptatem sequi nesciunt.”
    <svg class="quote-tail" width="30" height="22" viewBox="0 0 30 22"><path d="M0 0h28L2 20z" fill="#fff"/><path d="M2 0v20L28 0" fill="none" stroke="#e85b24" stroke-width="2"/></svg>
  </div>
  <div class="quote featured" style="left:440px">
    <div class="quote-icon"><svg width="18" height="16" viewBox="0 0 18 16"><path d="M2 2h14v9H7l-4 4v-4H2z" fill="#fff"/></svg></div>
    “Nemo enim ipsam voluptatem quia voluptas sit aspernatur aut odit aut fugit, sed quia con sequuntur magni dolores eos qui ratione vo luptatem sequi nesciunt.”
    <svg class="quote-tail" width="30" height="22" viewBox="0 0 30 22"><path d="M0 0h28L2 20z" fill="#e85b24"/></svg>
  </div>
  <div class="quote" style="left:779px">
    <div class="quote-icon"><svg width="18" height="16" viewBox="0 0 18 16"><path d="M2 2h14v9H7l-4 4v-4H2z" fill="#fff"/></svg></div>
    “Nemo enim ipsam voluptatem quia voluptas sit aspernatur aut odit aut fugit, sed quia con sequuntur magni dolores eos qui ratione vo luptatem sequi nesciunt.”
    <svg class="quote-tail" width="30" height="22" viewBox="0 0 30 22"><path d="M0 0h28L2 20z" fill="#fff"/><path d="M2 0v20L28 0" fill="none" stroke="#e85b24" stroke-width="2"/></svg>
  </div>
  <p class="quote-name" style="left:128px">- Delaney</p>
  <p class="quote-name" style="left:467px">- Mark Visser</p>
  <p class="quote-name" style="left:808px">- Harlow</p>
</section>

<footer class="site-footer">
  <div class="footer-brand">
    <div class="brand-dot"></div>
    <div class="name">GADGET HAVEN</div>
    <div class="tag">We will come to you!</div>
  </div>

  <div class="footer-col" style="left:263px">
    <h4>ORDERS &amp; RETURNS</h4>
    <ul class="links">
      <li>› Order Status</li>
      <li>› Shipping, Delivery &amp; Store Pickup</li>
      <li>› Return &amp; Exchange Promise</li>
      <li>› Price Match Guarantee</li>
      <li>› Pay With Points</li>
      <li>› More Orders &amp; Returns Help</li>
    </ul>
  </div>

  <div class="footer-col" style="left:535px">
    <h4>CONTACT US</h4>
    <div class="contact-row">
      <div class="c-icon"><svg width="14" height="18" viewBox="0 0 14 18"><path d="M7 1a6 6 0 0 1 6 6c0 5-6 10-6 10S1 12 1 7a6 6 0 0 1 6-6z" fill="#e85b24"/><circle cx="7" cy="7" r="2" fill="#fff"/></svg></div>
      <div><b>ADDRESS,</b><br>48 Harbor Lane<br>200 Westmoor, NL 3011</div>
    </div>
    <div class="contact-row">
      <div class="c-icon"><svg width="12" height="18" viewBox="0 0 12 18"><rect x="1" y="1" width="10" height="16" rx="2" fill="none" stroke="#e85b24" stroke-width="2"/></svg></div>
      <div><b>PHONE:</b><br>010 555 0148</div>
    </div>
    <div class="contact-row">
      <div class="c-icon"><svg width="16" height="12" viewBox="0 0 16 12"><rect x="1" y="1" width="14" height="10" fill="none" stroke="#e85b24" stroke-width="2"/><path d="M1 1l7 6 7-6" fill="none" stroke="#e85b24" stroke-width="2"/></svg></div>
      <div><b>Mail:</b><br>info@gadgethaven.com</div>
    </div>
  </div>

  <div class="footer-col" style="left:813px"><h4>CONTACT FORM</h4></div>
  <div class="field" style="left:815px;top:107px;width:136px;height:36px">Name</div>
  <div class="field" style="left:962px;top:107px;width:137px;height:36px">Phone</div>
  <div class="field" style="left:815px;top:153px;width:284px;height:63px">Message</div>
  <a class="btn send-btn">SEND MESSAGE</a>
</footer>

<div class="bottom-bar">
  <p class="copyright">Copyright © 2017 Gadget Haven. All Rights Reserved.</p>
  <div class="socials"><span></span><span></span><span></span><span></span><span></span></div>
</div>

</body>
</html>
```